New Logo and Business Card

Want new logo and business card for multi brand website. Attached are the logos for the back of the card.
We want a new logo for the front, the name "Tallvane" as the company name.
The logo can just be an "T" and a "V" for simplicity. With the text "Tallvane" after it.
For the business card use this info:
Doran Pelliske, PEng MBA
President
doran.pelliske@tallvane-mail.ca
+14035558213
Industry/Entity Type
Business
Logo Text
Tallvane
Logo styles of interest
Lettermark Logo

```html
<!DOCTYPE html>
<html lang="en">
<head>
<meta charset="utf-8">
<title>Tallvane – Business Card</title>
<link rel="stylesheet" href="https://fonts.googleapis.com/css2?family=Arimo:wght@400;700&display=swap">
<style>
  :root {
    --page-bg: #ffffff;
    --card-light: #cbcbcb;
    --card-dark: #9c9c9c;
    --ink-dark: #2e2e2e;
    --ink-mid: #1f1f1f;
    --ink-light: #ffffff;
    --emboss: rgba(255, 255, 255, 0.55);
  }
  html, body {
    margin: 0;
    padding: 0;
    width: 1200px;
    height: 900px;
    overflow: hidden;
    background: var(--page-bg);
  }
  .canvas {
    position: relative;
    width: 1200px;
    height: 900px;
  }
  .card {
    position: absolute;
    left: 100px;
    top: 235px;
    width: 1000px;
    height: 430px;
    border-radius: 48px;
    background: linear-gradient(200deg, var(--card-light) 0%, #b4b4b4 45%, var(--card-dark) 100%);
    box-shadow: 0 6px 18px rgba(0, 0, 0, 0.18);
    font-family: "Arimo", Arial, sans-serif;
  }
  .company-mark {
    position: absolute;
    right: 48px;
    top: 38px;
    display: flex;
    align-items: center;
    gap: 12px;
  }
  .company-dot {
    width: 22px;
    height: 22px;
    border-radius: 50%;
    background: var(--ink-dark);
  }
  .company-name {
    font-size: 30px;
    font-weight: 700;
    color: var(--ink-dark);
    line-height: 1;
  }
  .phone-row {
    position: absolute;
    left: 34px;
    top: 40px;
    display: flex;
    align-items: flex-start;
    gap: 10px;
  }
  .phone-row svg { width: 40px; height: 66px; margin-top: 6px; }
  .phone-number {
    font-size: 32px;
    color: var(--ink-mid);
    line-height: 1;
  }
  .identity {
    position: absolute;
    left: 230px;
    top: 100px;
    width: 540px;
    text-align: center;
  }
  .person-name {
    margin: 0;
    font-size: 60px;
    font-weight: 700;
    letter-spacing: 1px;
    color: var(--ink-dark);
    text-shadow: 0 2px 0 var(--emboss), 0 -1px 0 rgba(0,0,0,0.25);
    white-space: nowrap;
    line-height: 1.05;
  }
  .credentials, .role {
    margin: 0;
    font-size: 32px;
    color: var(--ink-light);
    line-height: 1.5;
  }
  .credentials { margin-top: 10px; }
  .email-row {
    position: absolute;
    left: 300px;
    top: 300px;
    display: flex;
    align-items: center;
    gap: 16px;
  }
  .email-row svg { width: 84px; height: 60px; }
  .email-address {
    font-size: 37px;
    color: var(--ink-mid);
    white-space: nowrap;
  }
</style>
</head>
<body>
<main class="canvas">
  <section class="card" aria-label="Tallvane business card">
    <div class="company-mark">
      <span class="company-dot" aria-hidden="true"></span>
      <span class="company-name">Tallvane</span>
    </div>

    <div class="phone-row">
      <svg viewBox="0 0 40 66" aria-hidden="true">
        <rect x="24" y="0" width="4" height="14" rx="1" fill="#1f1f1f"/>
        <rect x="2" y="10" width="34" height="54" rx="5" fill="#1f1f1f"/>
        <rect x="7" y="15" width="24" height="16" rx="1" fill="#d9d9d9"/>
        <g fill="#d9d9d9">
          <rect x="8" y="36" width="5" height="4"/><rect x="16.5" y="36" width="5" height="4"/><rect x="25" y="36" width="5" height="4"/>
          <rect x="8" y="43" width="5" height="4"/><rect x="16.5" y="43" width="5" height="4"/><rect x="25" y="43" width="5" height="4"/>
          <rect x="8" y="50" width="5" height="4"/><rect x="16.5" y="50" width="5" height="4"/><rect x="25" y="50" width="5" height="4"/>
        </g>
      </svg>
      <span class="phone-number">+14035558213</span>
    </div>

    <div class="identity">
      <h1 class="person-name">Doran Pelliske</h1>
      <p class="credentials">P.Eng. MBA</p>
      <p class="role">President</p>
    </div>

    <div class="email-row">
      <svg viewBox="0 0 84 60" aria-hidden="true">
        <rect x="2" y="2" width="80" height="56" rx="9" fill="#1f1f1f"/>
        <path d="M8 12 L42 38 L76 12" fill="none" stroke="#9c9c9c" stroke-width="4" stroke-linejoin="round"/>
      </svg>
      <span class="email-address">doran.pelliske@tallvane-mail.ca</span>
    </div>
  </section>
</main>
</body>
</html>
```